Email Design For Restwood Care

Need an email designed for a funeral home company called Restwood Care.
Final design needs to be delivered in HTML5 but can mock up design in any format.

CONCEPT/THEME

Design email for Pre-Planning Funeral Arrangements
Company is called Restwood Care Cemeteries and Funeral Homes

Email will target consumers that are interested in pre-planning for their funeral arrangements.

```html
<!DOCTYPE html>
<html lang="en">
<head>
<meta charset="utf-8">
<title>Restwood Care – Planning Ahead</title>
<link href="https://fonts.googleapis.com/css2?family=Cormorant+Garamond:wght@500;600&family=Libre+Franklin:wght@400;500;600;700&display=swap" rel="stylesheet">
<style>
:root{
  --blue:#3a62b3;
  --blue-deep:#2c4f9f;
  --navy:#2a4a8e;
  --gold:#8a7550;
  --gold-line:#b89a5c;
  --ink:#222;
  --white:#fff;
  --serif:'Cormorant Garamond', Georgia, serif;
  --sans:'Libre Franklin', Arial, sans-serif;
}
*{margin:0;padding:0;box-sizing:border-box}
html,body{width:1200px;height:4624px;overflow:hidden;background:var(--white)}
.email{position:relative;width:1200px;height:4624px;font-family:var(--sans);color:var(--ink)}
.abs{position:absolute}
.top-rule{left:0;top:0;width:1200px;height:5px;background:var(--gold)}
.brand{left:0;top:48px;width:1200px;text-align:center;font-family:var(--serif);font-weight:600;color:var(--navy);font-size:44px;line-height:1.05}
.brand small{display:block;font-size:30px}
.hero-band{left:0;top:359px;width:1200px;height:878px;background:linear-gradient(160deg,#3d66b8,#2f56a6)}
.hero-photo{left:75px;top:198px;width:1050px;height:532px;border-radius:26px;background:linear-gradient(120deg,#3f6b2e 0%,#6b4a2e 35%,#e9dcc4 60%,#d9c9a9 100%)}
.center{left:0;width:1200px;text-align:center;color:var(--white)}
.h1{font-family:var(--serif);font-weight:600;font-size:54px}
.divider{left:410px;width:380px;height:20px}
.lead{font-size:23px;line-height:53px}
.feature-icon{width:309px;height:253px;background:var(--white);border-radius:20px;box-shadow:0 8px 40px rgba(0,0,0,.12);display:flex;align-items:center;justify-content:center}
.feature-title{font-family:var(--serif);font-weight:600;font-size:42px;color:var(--ink)}
.feature-rule{width:117px;height:3px;background:var(--blue-deep)}
.feature-body{font-size:26px;line-height:52.5px;color:#2a2a2a}
.cta-band{left:0;top:3057px;width:1200px;height:646px;background:linear-gradient(160deg,#3d66b8,#2f56a6)}
.phone-pill{left:392px;top:3386px;width:416px;height:86px;border:3px solid var(--white);border-radius:43px;display:flex;align-items:center;color:var(--white);font-weight:700;font-size:36px}
.phone-pill .dot{width:66px;height:66px;border-radius:50%;background:var(--white);margin:0 20px 0 7px;display:flex;align-items:center;justify-content:center}
.promo{font-size:28px;line-height:52px}
.spanish{left:0;top:3703px;width:1200px;height:153px;background:var(--gold)}
.spanish-text{left:171px;top:3747px;font-family:var(--serif);font-weight:600;font-size:54px;color:var(--white)}
.learn-btn{left:691px;top:3745px;width:257px;height:79px;border:3px solid var(--white);border-radius:40px;color:var(--white);font-weight:700;font-size:27px;display:flex;align-items:center;justify-content:center}
.location-card{left:75px;top:3939px;width:1050px;height:486px;background:var(--white);box-shadow:0 8px 40px rgba(0,0,0,.12)}
.location-photo{left:75px;top:3939px;width:526px;height:486px;background:linear-gradient(180deg,#7ea4d6 0%,#dfe6ee 45%,#c9b59a 75%,#4e7a3a 100%)}
.loc-title{left:650px;top:3995px;font-family:var(--serif);font-weight:600;font-size:54px;color:var(--ink)}
.pin{left:645px;top:4101px;width:82px;height:82px;border-radius:50%;background:var(--blue-deep);display:flex;align-items:center;justify-content:center}
.address{left:650px;top:4205px;font-size:28px;line-height:52.5px;font-weight:500;color:var(--ink)}
.footer{left:0;top:4512px;width:1200px;height:112px;background:var(--blue-deep);color:var(--white)}
.social{left:110px;top:4512px;width:82px;height:82px;margin-top:0;border-radius:50%;background:var(--white);top:4512px}
.copyright{left:0;top:4541px;width:1200px;text-align:center;font-size:20px;color:var(--white);line-height:24px}
.code{left:1105px;top:4541px;font-size:20px;color:var(--white)}
</style>
</head>
<body>
<div class="email">
  <div class="abs top-rule"></div>
  <div class="abs brand">Coral Grove<small>Park Cemetery</small></div>

  <div class="abs hero-band" role="img" aria-label="Soft blue-tinted background photo of flowers and a notebook"></div>
  <div class="abs hero-photo" role="img" aria-label="Photo of a to-do list notebook with roses and a pink pen on a wooden desk"></div>

  <div class="abs center h1" style="top:800px">Planning Ahead Can Make All the Difference</div>
  <svg class="abs divider" style="top:900px" viewBox="0 0 380 20"><line x1="0" y1="10" x2="150" y2="10" stroke="#b89a5c" stroke-width="2"/><line x1="230" y1="10" x2="380" y2="10" stroke="#b89a5c" stroke-width="2"/><circle cx="190" cy="10" r="5" fill="#b89a5c"/></svg>
  <p class="abs center lead" style="top:942px">It’s not easy to talk about your end-of-life wishes before you have to. But it’s one of the<br>most important conversations you’ll ever have with your loved ones. By preplanning your<br>funeral, you can make sure your life is celebrated the way you want, and give your loved<br>ones the peace-of-mind they need when the time comes.</p>

  <!-- Feature 1 -->
  <div class="abs feature-icon" style="left:131px;top:1377px">
    <svg width="200" height="170" viewBox="0 0 200 170" fill="none" stroke="#2f56a6" stroke-width="8" stroke-linejoin="round" stroke-linecap="round"><path d="M20 150 L150 150 L180 140 L180 80 L110 70 L60 60 L30 110 Z"/><path d="M90 20 L120 40 L75 115 L55 120 L60 98 Z"/><circle cx="40" cy="150" r="10"/><circle cx="62" cy="150" r="10"/></svg>
  </div>
  <div class="abs feature-title" style="left:577px;top:1338px">Put Your Wishes in Writing</div>
  <div class="abs feature-rule" style="left:577px;top:1408px"></div>
  <p class="abs feature-body" style="left:577px;top:1452px">You want your funeral to be meaningful,<br>right? By sharing your end-of-life wishes,<br>you’ll ensure your funeral will truly reflect<br>you and your life.</p>

  <!-- Feature 2 -->
  <div class="abs feature-title" style="left:75px;top:1753px">Eliminate stress for your loved ones</div>
  <div class="abs feature-rule" style="left:86px;top:1824px"></div>
  <p class="abs feature-body" style="left:86px;top:1869px">By prearranging your funeral, you can alleviate<br>the stress and burden of making tough deci-<br>sions at an already difficult time for them.</p>
  <div class="abs feature-icon" style="left:792px;top:1794px">
    <svg width="170" height="210" viewBox="0 0 170 210" fill="none" stroke="#2f56a6" stroke-width="7" stroke-linejoin="round" stroke-linecap="round"><path d="M70 200 L70 170 Q30 160 32 130 L15 115 L30 100 Q25 45 80 40 Q130 40 140 90 Q142 130 120 150 L120 200"/><path d="M120 10 L95 55 L120 55 L100 95 L150 45 L125 45 L140 10 Z"/></svg>
  </div>

  <!-- Feature 3 -->
  <div class="abs feature-icon" style="left:131px;top:2204px">
    <svg width="200" height="200" viewBox="0 0 200 200" fill="none" stroke="#2f56a6" stroke-width="7" stroke-linecap="round"><rect x="70" y="10" width="60" height="40"/><rect x="70" y="150" width="60" height="40"/><circle cx="100" cy="100" r="52"/><circle cx="100" cy="100" r="38"/><path d="M112 82 Q100 72 90 82 Q85 95 100 100 Q115 105 110 118 Q100 128 88 118 M100 70 V130"/><path d="M160 60 Q175 75 175 95 M172 45 Q192 68 192 95"/><path d="M40 140 Q25 125 25 105 M28 155 Q8 132 8 105"/></svg>
  </div>
  <div class="abs feature-title" style="left:577px;top:2163px">Save Time And Money</div>
  <div class="abs feature-rule" style="left:577px;top:2233px"></div>
  <p class="abs feature-body" style="left:577px;top:2278px">Protect your loved ones from inflation by lock-<br>ing in today’s prices for the funeral you truly<br>want. Your expenses will be taken care of<br>when you need them to be, guaranteed.</p>

  <!-- Feature 4 -->
  <div class="abs feature-title" style="left:80px;top:2578px">Personalize Your Service</div>
  <div class="abs feature-rule" style="left:80px;top:2649px"></div>
  <p class="abs feature-body" style="left:80px;top:2694px">It’s your funeral, so celebrate your life, your<br>way. By preplanning, you can choose your<br>own funeral services, including songs, read-<br>ings or other personal details that are im-<br>portant to you.</p>
  <div class="abs feature-icon" style="left:792px;top:2619px">
    <svg width="180" height="180" viewBox="0 0 180 180" fill="none" stroke="#2f56a6" stroke-width="6" stroke-linejoin="round" stroke-linecap="round"><rect x="110" y="10" width="60" height="44" rx="6"/><path d="M125 25 H155 M125 38 H148"/><path d="M40 90 Q30 40 70 40 Q100 45 90 90"/><path d="M10 170 V135 Q15 110 45 105 L65 135 L85 105 Q100 108 110 120"/><path d="M100 170 L115 130 L160 115"/></svg>
  </div>

  <!-- Call to action -->
  <div class="abs cta-band" role="img" aria-label="Soft blue-tinted background photo of flowers and a notebook"></div>
  <div class="abs center h1" style="top:3152px;line-height:61px">Call Today to Learn More From the<br>Safety of Your Home</div>
  <svg class="abs divider" style="top:3322px" viewBox="0 0 380 20"><line x1="0" y1="10" x2="150" y2="10" stroke="#b89a5c" stroke-width="2"/><line x1="230" y1="10" x2="380" y2="10" stroke="#b89a5c" stroke-width="2"/><circle cx="190" cy="10" r="5" fill="#b89a5c"/></svg>
  <div class="abs phone-pill"><span class="dot"><svg width="32" height="32" viewBox="0 0 24 24"><path fill="#2f56a6" d="M6.6 10.8a15 15 0 006.6 6.6l2.2-2.2c.3-.3.7-.4 1-.2 1.1.4 2.3.6 3.6.6.6 0 1 .4 1 1V20c0 .6-.4 1-1 1A17 17 0 013 4c0-.6.4-1 1-1h3.5c.6 0 1 .4 1 1 0 1.3.2 2.5.6 3.6.1.3 0 .7-.2 1z"/></svg></span>(305) 555-0142</div>
  <p class="abs center promo" style="top:3516px">Mention this email and get an additional 5% our Spring Savings<br>with promo code <b>CGPSpring2021</b></p>

  <!-- Spanish band -->
  <div class="abs spanish"></div>
  <div class="abs spanish-text">Se Habla Español</div>
  <div class="abs learn-btn">Learn More</div>

  <!-- Location -->
  <div class="abs location-card"></div>
  <div class="abs location-photo" role="img" aria-label="Photo of the cemetery entrance building under a cloudy sky with palm trees"></div>
  <div class="abs loc-title">Include Location</div>
  <div class="abs pin"><svg width="26" height="34" viewBox="0 0 24 32"><path fill="#fff" d="M12 0C5.4 0 0 5.4 0 12c0 9 12 20 12 20s12-11 12-20C24 5.4 18.6 0 12 0zm0 16a4 4 0 110-8 4 4 0 010 8z"/></svg></div>
  <p class="abs address">Coral Grove Park&nbsp; Cemetery<br>4810 SW 52nd Avenue<br>Miami, FL 33155</p>

  <!-- Footer -->
  <div class="abs footer"></div>
  <div class="abs social" style="top:4512px;margin-top:0;transform:translateY(0);top:4512px"></div>
  <div class="abs copyright">© Copyrights 2021 Company Name&nbsp;&nbsp; |&nbsp;&nbsp; All Rights Reserved</div>
  <div class="abs code">C 43</div>
</div>
</body>
</html>
```